Tidewell Vertical Estate Council revised design

We need a logo for our email and letterhead design. We are a non-profit home owners association looking to look a little more professional. Attached is our current "logo" but it doesn't work well with letters or email. We would like to stay with the same concept.

Target Market(s)

Home owners, attorney, bankers, legislators

Industry/Entity Type

Non Profit

Font styles to use
Sans Serif

Colors

Designer to choose colors to be used in the design.

Requirements
Must have
• Company name: Tidewell Vertical Estate Council
Nice to have
• This will always be on a while background (paper or email)

```html
<!DOCTYPE html>
<html lang="en">
<head>
<meta charset="utf-8">
<title>Tidewell Vertical Estate Council — Letterhead</title>
<link rel="stylesheet" href="https://fonts.googleapis.com/css2?family=Montserrat:wght@400;600;700&family=Open+Sans:wght@400;600&display=swap">
<style>
  :root {
    --backdrop: #e9eaec;
    --paper: #ffffff;
    --ink: #33373c;
    --ink-soft: #6b7078;
    --navy: #1d5b84;
    --sky: #3e9fd2;
    --teal: #2a7fa6;
    --ring: #b9bec4;
  }
  * { box-sizing: border-box; margin: 0; padding: 0; }
  html, body { width: 1200px; height: 832px; overflow: hidden; }
  body {
    background: var(--backdrop);
    font-family: "Open Sans", Arial, sans-serif;
    color: var(--ink);
    position: relative;
  }
  .letterhead {
    position: absolute;
    left: 150px; top: 20px;
    width: 560px; height: 792px;
    background: var(--paper);
    box-shadow: 0 6px 24px rgba(0,0,0,.12);
    padding: 56px 52px 0;
  }
  .letterhead__brand {
    position: absolute; top: 44px; right: 48px;
    display: flex; align-items: center; gap: 10px;
  }
  .brand-dot {
    width: 38px; height: 38px; border-radius: 50%;
    border: 2px solid var(--ring);
    flex: none;
  }
  .brand-name {
    font-family: "Montserrat", Arial, sans-serif;
    font-weight: 700; font-size: 11px; line-height: 1.25;
    color: var(--teal); text-transform: uppercase; letter-spacing: .04em;
    width: 110px;
  }
  .recipient {
    margin-top: 40px;
    font-size: 9.5px; line-height: 1.5; font-style: normal;
  }
  .recipient .recipient__name { font-weight: 600; }
  .letter-body {
    margin-top: 34px;
    font-size: 8.5px; line-height: 1.7; color: var(--ink-soft);
    width: 420px;
  }
  .letter-body p { margin-bottom: 14px; }
  .signoff { margin-top: 22px; font-size: 8.5px; color: var(--ink-soft); }
  .signature {
    display: block; width: 110px; height: 38px; margin: 8px 0 4px;
    background: linear-gradient(90deg, #d9dadc, #eeeeef);
    border-radius: 3px;
  }
  .signer { font-size: 8px; color: var(--ink-soft); }
  .letterhead__footer {
    position: absolute; left: 0; right: 0; bottom: 0;
  }
  .contact-line {
    padding: 0 52px 14px;
    font-size: 8px; color: var(--ink-soft); letter-spacing: .02em;
    white-space: nowrap;
  }
  .contact-line span + span::before { content: "|"; margin: 0 10px; color: var(--navy); }
  .footer-band { display: flex; height: 14px; }
  .footer-band__main { flex: 1; background: var(--navy); }
  .footer-band__accent { width: 90px; background: var(--sky); }

  .logo-lockup {
    position: absolute; left: 790px; top: 370px;
    display: flex; align-items: center; gap: 18px;
  }
  .logo-lockup .brand-dot { width: 84px; height: 84px; border-width: 3px; }
  .logo-lockup .brand-name { font-size: 22px; width: 250px; }
</style>
</head>
<body>
  <main class="letterhead">
    <div class="letterhead__brand">
      <span class="brand-dot"></span>
      <span class="brand-name">Tidewell Vertical Estate Council</span>
    </div>

    <address class="recipient">
      To<br>
      <span class="recipient__name">Mr. Daniel Ortis</span><br>
      Chief Executive Officer<br>
      Harbor Lane Designs<br>
      18 Ocean Street<br>
      Eastport, Maine 04631
    </address>

    <section class="letter-body">
      <p>Thank you for your continued support of our community. This letter shares a short update on the projects our council has planned for the coming season, including roof repairs, pool resurfacing and new lighting along the north walkway.</p>
      <p>All owners are invited to the annual meeting in the clubhouse, where the board will review the budget, answer questions and collect votes on the proposed changes to the shared grounds and parking rules.</p>
      <p>Please contact the office with any concerns before the end of the month. We look forward to seeing you there.</p>
    </section>

    <div class="signoff">
      Yours faithfully
      <span class="signature" role="img" aria-label="Handwritten signature"></span>
      <span class="signer">Jane Marlow</span>
    </div>

    <footer class="letterhead__footer">
      <div class="contact-line">
        <span>(555) 014-2280</span><span>PO Box 410 Harbor Point, Maine 04011</span><span>www.tidewellcouncil.org</span>
      </div>
      <div class="footer-band">
        <div class="footer-band__main"></div>
        <div class="footer-band__accent"></div>
      </div>
    </footer>
  </main>

  <div class="logo-lockup">
    <span class="brand-dot"></span>
    <span class="brand-name">Tidewell Vertical Estate Council</span>
  </div>
</body>
</html>
```